Heath Weight Loss Retreat Website

The brief:
PineLoop is a provider of health & weight loss retreats and wish to redesign their main website. The website needs to provide detailed information about the company’s services whilst gathering the maximum number of leads possible. The website does not aim to get clients to ‘book now’ but to request further information, or ask a question generating a lead/opportunity for the business.

Primary objectives of website
• Gather leads for products (not necessarily to book at that point, but to ‘request more info’)
• Provide detailed information about the health and fitness programs on offer

Demographic Considerations
• Target age group: 30-50
• Predominant client base are female but website should be gender neutral due to some men attending

Design considerations
• Essentially selling ‘travel experiences’ and ‘life transformations’ so needs to be lots of images to display (similar to a hotel website for example)
• Images need to display real people – i.e. larger people, rather than super thin
• Not too much use of flash
• SEO friendly (we have good rankings at present)
• Will be implemented into Joomla, so please consider this on the design
• Colours should be ‘warm’ and ‘friendly’ and gender neutral

Project Requirements & Expectations
Please supply your design ideas with:
• At least 1 (preferably more) homepage examples
• At least 1 (preferably more) internal page examples
Once a preferred design has been selected the following will be produced, tweaked and approved:
• Homepage + 1 internal landing page + 1 internal main page + 1 contact page + 1 info request page

Attachments
We have attached both a homepage and internal page example which demonstates the type of content needed and the calls to action. This is for demonstration purposes only so please ignore colours, fonts, etc and provide your best designs based on a general layout as per attached.

Images:
A selection of example images has been attached. For the homepage images of the retreats themselves should be used alongside images of ‘larger people’.

Further information:
Please contact Simon Thackery at simon.thackery@coralbeaconfiles.com.au

Target Market(s)

Overweight females aged 30-50 are the main target market. However must be gender neutral due to some men using product.

Industry/Entity Type

Weight

Requirements
Should not have
• Not too much flash

```html
<!DOCTYPE html>
<html lang="en">
<head>
<meta charset="utf-8">
<title>PineLoop Weight Loss Retreat</title>
<link href="https://fonts.googleapis.com/css2?family=Arimo:ital,wght@0,400;0,700;1,400;1,700&display=swap" rel="stylesheet">
<style>
:root{
  --green:#5a9a2a;
  --green-dark:#2c7a1c;
  --green-pale:#e5f7d6;
  --green-soft:#d2efbc;
  --orange:#f08c00;
  --peach:#fdd899;
  --peach-edge:#e9a640;
  --text:#111;
  --panel:#fff;
  --shadow:#cfe6bf;
}
*{box-sizing:border-box;margin:0;padding:0}
html,body{width:873px;height:1200px;overflow:hidden;background:#fff}
body{font-family:"Arimo",Arial,sans-serif;color:var(--text);font-size:12px}
.page{position:absolute;left:0;top:0;width:960px;height:1320px;transform:scale(.909375);transform-origin:0 0}
a{color:var(--orange);text-decoration:underline}
.abs{position:absolute}
.panel{position:absolute;background:var(--panel);border-radius:10px;box-shadow:0 0 0 3px var(--shadow)}
.logo{left:28px;top:22px;display:flex;align-items:center;gap:8px}
.logo .dot{width:28px;height:28px;border-radius:50%;background:var(--orange)}
.logo .name{font-size:26px;font-weight:700;color:var(--green)}
.banner{left:240px;top:10px;width:480px;height:60px;background:#eee;border:1px solid #ddd;box-shadow:2px 2px 3px #ccc;display:flex;align-items:center;justify-content:center;font-size:22px;font-weight:700;color:#fff;text-shadow:0 0 2px #999}
.social{left:760px;top:20px;display:flex;gap:16px}
.social span{width:32px;height:32px;border-radius:4px;background:var(--green)}
.nav{left:0;top:81px;width:960px;height:28px;background:var(--green-pale);border-top:4px solid var(--green-dark);border-bottom:3px solid var(--green-dark);display:flex;align-items:center;font-size:12px}
.nav span{position:absolute}
.nav .caret{width:0;height:0;border:5px solid transparent;border-top:6px solid #333;border-bottom:none}
.tree{left:10px;top:120px;width:210px;height:380px;background:var(--green-pale);padding:10px 0 0 14px;font-size:12px;line-height:14.4px}
.tree .top{font-weight:700;border-left:1px solid #666;padding-left:3px}
.tree .sub{margin-left:16px;border-left:1px solid #666;padding-left:3px}
.tree .home{color:var(--orange)}
.goal{left:10px;top:508px;width:210px;height:110px}
.goal .inner{position:absolute;left:6px;top:6px;right:6px;bottom:6px;background:var(--peach);border:1px solid var(--peach-edge);padding:8px 8px}
.goal h3{color:var(--green);font-size:17px}
.goal p{font-style:italic;font-size:12px;line-height:14px}
.goal .field{display:flex;gap:8px;margin-top:6px}
.goal .field span{width:146px;height:22px;background:#fff;border:1px solid #999}
.goal .field b{font-weight:400;font-style:italic;border:1px solid #999;background:#fff;padding:3px 6px;font-size:12px}
.results{left:10px;top:632px;width:210px;height:366px;background:var(--peach);padding:10px 14px}
.results h3{color:var(--green);font-size:18px;line-height:22px}
.results ul{list-style:none;margin-top:20px;font-size:12px;line-height:14.5px}
.results li{padding-left:14px;text-indent:-8px}
.hero{left:230px;top:120px;width:500px;height:278px}
.hero .photo{position:absolute;left:9px;top:9px;width:482px;height:262px;background:linear-gradient(160deg,#3a4a2e 0%,#6f8a4a 35%,#d9e6e8 55%,#587a3a 80%,#2e3c22 100%)}
.hero .cap{position:absolute;left:15px;top:196px;width:470px;height:66px;background:rgba(246,236,200,.85);border:1px solid #c9a43a;padding:4px 12px;font-size:11px;line-height:13px}
.hero .cap h4{color:var(--green);font-size:14px}
.hero .cap i{display:block;font-size:12px;margin-left:14px}
.hero .cap p{margin-left:24px}
.people{left:230px;top:410px;width:500px;height:158px}
.thumb{position:absolute;background:linear-gradient(#a88b6c,#6c5038)}
.people h3{position:absolute;left:216px;top:24px;color:var(--green);font-size:17px}
.people ul{position:absolute;left:252px;top:48px;list-style:none;font-size:12px;line-height:15px}
.people a{position:absolute;left:216px;top:106px;font-style:italic;font-size:12px}
.cta{left:230px;top:580px;width:500px;height:178px}
.cta .inner{position:absolute;left:11px;top:11px;right:9px;bottom:9px;background:var(--green-pale);border:1px solid #9cc87a;padding:8px 6px}
.cta .lead{font-style:italic;font-weight:700;font-size:13px}
.cta .quote{font-style:italic;font-weight:700;font-size:21px;letter-spacing:-.3px;white-space:nowrap;color:var(--green);margin-top:6px}
.btn{position:absolute;top:71px;height:24px;background:linear-gradient(#fde0a0,#f4b247);border:1px solid #d48a20;border-radius:4px;font-weight:700;font-size:14px;display:flex;align-items:center;justify-content:center}
.cta .cols{position:absolute;top:113px;font-weight:700;font-size:12px;line-height:15px}
.life{left:230px;top:770px;width:500px;height:500px;padding:13px 12px}
.life h2{color:var(--green);font-size:18px;padding-bottom:10px;border-bottom:1px solid #333}
.life p{font-size:12px;line-height:14.5px;margin:0 10px 14px 21px}
.life .block{padding-top:10px}
.life hr{border:none;border-top:1px solid #333;border-bottom:1px solid #333;height:4px;margin:-2px 0 0}
.mag{left:740px;top:120px;width:210px;height:120px}
.mag .cover{position:absolute;left:18px;top:8px;width:70px;height:100px;background:linear-gradient(150deg,#1d2b6e,#ffffff 50%,#e04a6a);transform:rotate(-8deg)}
.mag .txt{position:absolute;left:95px;top:30px;font-size:12px}
.mag .txt b{display:block;color:var(--green);font-size:19px;font-style:italic}
.mag .txt strong{color:var(--green)}
.mag .txt a{font-style:italic;display:block}
.testi{left:740px;top:250px;width:210px;height:150px}
.testi .box{position:absolute;left:8px;top:27px;width:194px;height:94px;background:var(--green-pale);border:1px solid var(--peach-edge);padding:6px 8px;font-style:italic;color:var(--green);font-size:18px;line-height:22px;text-align:center}
.testi .box small{display:block;text-align:left;color:var(--orange);font-size:12px;line-height:14px}
.locs{left:740px;top:410px;width:210px;height:285px;padding:12px 10px}
.locs h3{color:var(--green);font-size:18px}
.locs i{font-weight:700;font-size:13px}
.loc{position:absolute;left:4px;width:202px;height:62px;background:linear-gradient(#8ab0d6,#c7d9c0 60%,#4f7a3a);padding:6px 10px;font-size:12px}
.loc b{display:block;font-size:12px}
.loc em{display:block;font-size:8px;line-height:10px}
.loc u{font-size:8px;font-weight:700;color:#1f3a80}
.progs{left:740px;top:710px;width:210px;height:558px;padding:14px 13px;font-size:12px;line-height:14.5px}
.progs h3{color:var(--green);font-size:18px;line-height:20px}
.progs h4{color:var(--green);font-size:12px;margin-top:28px}
.progs .top{font-style:italic}
.progs .desc{font-style:italic}
.progs .trainer{white-space:nowrap;font-size:11.5px;letter-spacing:-.2px}
.foot{left:0;top:1281px;width:960px;height:31px;border-top:3px solid var(--green-dark);border-bottom:3px solid var(--green-dark);font-size:11px}
.foot .copy{position:absolute;left:26px;top:9px}
.foot .links{position:absolute;right:28px;top:7px}
.foot .links a{color:var(--green-dark)}
.arrow{position:absolute;width:0;height:0;border:16px solid transparent}
</style>
</head>
<body>
<div class="page">
  <div class="abs logo"><span class="dot"></span><span class="name">PineLoop</span></div>
  <div class="abs banner">Posible Banner</div>
  <div class="abs social" aria-label="Social links"><span></span><span></span><span></span><span></span></div>

  <nav class="abs nav">
    <span style="left:34px">Home</span>
    <span style="left:136px">About Us</span><i class="abs caret" style="left:218px;top:9px"></i>
    <span style="left:254px;text-decoration:underline">The Best Programs</span><i class="abs caret" style="left:393px;top:9px"></i>
    <span style="left:429px">To Know More</span><i class="abs caret" style="left:539px;top:9px"></i>
    <span style="left:575px">Free Information</span><i class="abs caret" style="left:697px;top:9px"></i>
    <span style="left:733px">Contact Us</span>
    <span style="left:862px">Book Now</span>
  </nav>

  <aside class="panel tree">
    <div class="top home">Home</div>
    <div class="top">About Us</div>
    <div class="sub">Why Choose PineLoop<br>Our Team<br>Our Clients<br>What Our Clients Said<br>Results Our Clients Achived</div>
    <div class="top">The Best Programs</div>
    <div class="sub">Weight Loss Retreat<br>Residential Boot Camp<br>Fitness Days<br>At Home Program<br>Local Group Exercise</div>
    <div class="top">To Know More</div>
    <div class="sub">Weight Loss<br>Fitness Goals<br>Diabetes Reduction<br>Blood Pressure Reduction<br>Depression Improvement<br>More Health Benefits</div>
    <div class="top">Free Information</div>
    <div class="sub">Request a Brochure<br>FREE PineLoop Magazine</div>
    <div class="top">Contact Us</div>
    <div class="top">Book Now</div>
  </aside>

  <div class="panel goal"><div class="inner">
    <h3>Your Goal Selector</h3>
    <p>Tell us your goal and we'll tell you how PineLoop can help:</p>
    <div class="field"><span></span><b>Go</b></div>
  </div></div>

  <div class="panel results">
    <h3>Results our clients have Achived</h3>
    <ul>
      <li>- Weight loss</li><li>- Fat loss</li>
      <li>- Lose centimetres of your waist, hips, thighs and from all over your boty</li>
      <li>- Increased flexibility</li><li>- Improved mobility and agility</li>
      <li>- Transform your skin condition</li><li>- Feel happier</li>
      <li>- Better sleep patterns</li><li>- Eliminate high blood pressure</li>
      <li>- Eliminate Type 2 Diabetes</li><li>- Reduce cholesterol issues</li>
      <li>- Improve previous injuries</li><li>- Reduce head aches</li>
      <li>- Reduce stress</li><li>- No more anxiety</li>
      <li>- Significant improvements for those suffering depression</li>
    </ul>
  </div>

  <section class="panel hero">
    <div class="photo" role="img" aria-label="Waterfall in a lush green rainforest at the retreat"></div>
    <div class="cap">
      <h4>Amazing weight loss &amp; fitness results</h4>
      <i>Lasting results &amp; 1st class facilities</i>
      <p>PineLoop has helped hundreds of people transform their lives, lose weight, get fit and achieve lasting success. Let us help you too... <a href="#" style="float:right">Read More&gt;&gt;</a></p>
    </div>
  </section>

  <section class="panel people">
    <div class="thumb" style="left:27px;top:13px;width:80px;height:60px" role="img" aria-label="Client relaxing with a book"></div>
    <div class="thumb" style="left:118px;top:13px;width:72px;height:60px" role="img" aria-label="Smiling client portrait"></div>
    <div class="thumb" style="left:27px;top:80px;width:75px;height:64px" role="img" aria-label="Client outdoors"></div>
    <div class="thumb" style="left:118px;top:80px;width:72px;height:64px" role="img" aria-label="Client portrait"></div>
    <h3>Real People - Real Results</h3>
    <ul><li>- 100's of people helped by PineLoop</li><li>- People of all ages, shapes, and sizes</li><li>- Normal people just like you</li></ul>
    <a href="#">Testimonials and reviews&gt;&gt;</a>
  </section>

  <section class="panel cta"><div class="inner">
    <div class="lead">The PineLoop program works - as one client put it...</div>
    <div class="quote">“The Best Weight loss Experience of my life”</div>
    <div class="btn" style="left:6px;width:287px">Request a FREE information pack &gt;&gt;</div>
    <div class="btn" style="left:302px;width:170px">More Testimonials</div>
    <div class="cols" style="left:40px">- Stunning Locations<br>- 1st class facilities</div>
    <div class="cols" style="left:185px">- Amazing results<br>- For al shapes &amp; sizes</div>
    <div class="cols" style="left:328px">- Delicious healty food<br>- Expert Support</div>
  </div></section>

  <section class="panel life">
    <h2>PineLoop Transforms Your Life</h2>
    <div class="block">
      <p>Hundreds of people hhave already transformed their lives with PineLoop's proven programs. With PineLoop you will lose weight, lose centimetres, get fit and experience lasting health and fitness results.</p>
      <p>Our <a href="#"><i>Weight Loss Retreat</i></a> program is suitable for people of all ages, shapes, sizes and fitness levels. It is amazingly fun and extremely effective with amazing weight loss and fitness results. Whether you want a kick start or are embarking on a long term weight loss program our <a href="#"><i>Weight Loss Retreat</i></a> program will be one of the best experiences of your life - that's our promise to you.</p>
    </div>
    <hr>
    <div class="block">
      <p>Hundreds of people hhave already transformed their lives with PineLoop's proven programs. With PineLoop you will lose weight, lose centimetres, get fit and experience lasting health and fitness results.</p>
      <p>Our <a href="#"><i>Weight Loss Retreat</i></a> program is suitable for people of all ages, shapes, sizes and fitness levels. It is amazingly fun and extremely effective with amazing weight loss and fitness results. Whether you want a kick start or are embarking on a long term weight loss program our <a href="#"><i>Weight Loss Retreat</i></a> program will be one of the best experiences of your life - that's our promise to you.</p>
    </div>
    <hr>
    <div class="block">
      <p>Hundreds of people hhave already transformed their lives with PineLoop's proven programs. With PineLoop you will lose weight, lose centimetres, get fit and experience lasting health and fitness results.</p>
      <p>Our <a href="#"><i>Weight Loss Retreat</i></a> program is suitable for people of all ages, shapes, sizes and fitness levels. It is amazingly fun and extremely effective with amazing weight loss and fitness results. Whether you want a kick start or are embarking on a long term weight loss program our <a href="#"><i>Weight Loss Retreat</i></a> program will be one of the best experiences of your life - that's our promise to you.</p>
    </div>
  </section>

  <aside class="panel mag">
    <div class="cover" role="img" aria-label="Magazine cover"></div>
    <div class="txt"><b>FREE</b><strong>PineLoop Magazine</strong><a href="#">Request Now &gt;&gt;</a></div>
  </aside>

  <aside class="panel testi">
    <i class="arrow" style="left:87px;top:-13px;border-bottom-color:#000"></i>
    <div class="box">“The best weight loss experience in my life”<small>(Name of the person)</small></div>
    <i class="arrow" style="left:91px;top:128px;border-top-color:#000"></i>
  </aside>

  <aside class="panel locs">
    <h3>The Best Locations</h3>
    <i>&amp; 1<sup>st</sup> class facilities</i>
    <div class="loc" style="top:64px" role="img" aria-label="Blue Mountains retreat scenery"><b>Blue Mountains ****</b><em>4 star accommodation, stunning mountain scenery &amp; 1st class facilities</em><u>Find out more | FREE Brochure | Book</u></div>
    <div class="loc" style="top:144px" role="img" aria-label="Sunshine Coast beach scenery"><b style="color:#fff">Sunshine Coast ****</b><em style="color:#fff">4 star accommodation</em><u>Find out more | FREE Brochure | Book</u></div>
    <div class="loc" style="top:215px" role="img" aria-label="Sunshine Coast beach scenery"><b style="color:#fff">Sunshine Coast ****</b><em style="color:#fff">4 star accommodation</em><u>Find out more | FREE Brochure | Book</u></div>
  </aside>

  <aside class="panel progs">
    <h3>The Best Programs</h3>
    <a href="#" class="top">Book Now&gt;&gt;</a>
    <h4>Weight Loss Retreat</h4><div class="desc">Lasting weight loss results</div>
    <a href="#">Program details</a> | <a href="#">Typical Day</a><br><a href="#">Dates &amp; Rates</a> | <a href="#">FREE Brochure</a>
    <h4>Residential Boot Camp</h4><div class="desc">Kick start your health &amp; fitness</div>
    <a href="#">Program details</a> | <a href="#">Typical Day</a><br><a href="#">Dates &amp; Rates</a> | <a href="#">FREE Brochure</a>
    <h4>At Home Program</h4><div class="desc">Do it yourself with our home pack</div>
    <a href="#">Program details</a> | <a href="#">FREE Brochure</a>
    <h4>Fitness Days</h4><div class="desc">Have fun and keep on track</div>
    <a href="#">Program overview</a> | <a href="#">Typical Day</a><br><a href="#">Dates &amp; Rates</a> | <a href="#">FREE Brochure</a>
    <h4>Local Group Exercise</h4><div class="desc">Get fit &amp; lose weight locally</div>
    <a href="#">Overview</a> | <a href="#">Tipes &amp; Locations</a>
    <h4>Personal Training for you</h4>
    <a href="#" class="trainer">Find an approved PineLoop Trainer</a>
  </aside>

  <footer class="abs foot">
    <span class="copy">Copyright PineLoop Wellbeing PTY Ltd &nbsp;|&nbsp; ABN 9876512340</span>
    <span class="links"><a href="#">Contact Us</a> &nbsp;|&nbsp; <a href="#">Book Now</a> &nbsp;|&nbsp; <a href="#">FAQ</a> &nbsp;|&nbsp; <a href="#">Privacy</a></span>
  </footer>
</div>
</body>
</html>
```